Kobalto Cell Phone Repair

We are a small cell phone repair store in need of a redesign to our current business card to make it a more modern, cleaner design that will catch folks' attention (perhaps with rounded edges ) - But still include most of the information listed on the current card. Would like to keep the current color scheme of black/white and green. Card will not need any personnel name included. Would like to see some designs include takes on a velorin or tekvo screen as well as more traditional cards.

Target Market(s)

broad spectrum across all cell phone users

Industry/Entity Type

Cell Phone

Contact Information for Business Card

changes to front text:
keep business Logo
business address, phone number website and email. All other info optional (add gathernest and blurvo icons on card

Rear of card:

Keep repair services, change tekvo repair to slatra repair, change quorvex os repair to data recovery (with appropriate icon or substitute)
remove products text
remove pjw and ravesh from manufacturer logos, add dunbelio.

Requirements
Must have
• business Logo
• business address, phone number website and email
• keep colors to white/black/green/gray
• gathernest and blurvo icons on card
Nice to have
• Would like to see 'traditional' business card design as well as creative design incorporating incorporating front of cell phone (eg tekvo or quorvex). Rounded edges would be nice but not necessary.

```html
<!DOCTYPE html>
<html lang="en">
<head>
<meta charset="utf-8">
<title>Kobalto Cell Phone Repair – Business Card</title>
<link rel="stylesheet" href="https://fonts.googleapis.com/css2?family=Roboto+Condensed:wght@700&family=Varela+Round&display=swap">
<style>
  :root {
    --green: #7cc243;
    --green-dark: #5a9a2c;
    --ink: #1d1d1d;
    --charcoal: #2a2a2a;
    --white: #ffffff;
    --gray: #8a8a8a;
    --page: #e6e7e8;
  }
  * { margin: 0; padding: 0; box-sizing: border-box; }
  html, body { width: 1200px; height: 1200px; overflow: hidden; }
  body { background: var(--page); position: relative; font-family: "Varela Round", sans-serif; }

  .card { position: absolute; top: 170px; width: 430px; height: 860px; border-radius: 64px; overflow: hidden; }

  /* Front */
  .card--front { left: 140px; background: var(--green); }
  .front__speaker { position: absolute; top: 58px; left: 175px; width: 80px; height: 8px; border-radius: 4px; background: var(--ink); }
  .front__sensor { position: absolute; top: 38px; left: 210px; width: 10px; height: 10px; border-radius: 50%; background: var(--ink); }
  .front__camera { position: absolute; top: 54px; left: 130px; width: 16px; height: 16px; border-radius: 50%; background: var(--ink); }
  .front__screen { position: absolute; top: 110px; left: 28px; width: 374px; height: 600px; background: var(--white); padding: 34px 26px 24px; display: flex; flex-direction: column; }
  .front__home { position: absolute; bottom: 40px; left: 180px; width: 70px; height: 70px; border-radius: 50%; background: var(--white); border: 3px solid #cfcfcf; }

  .brand { display: flex; align-items: center; gap: 14px; margin-bottom: 14px; }
  .brand__dot { width: 44px; height: 44px; border-radius: 50%; background: var(--green); flex: none; }
  .brand__name { font-family: "Roboto Condensed", sans-serif; font-weight: 700; font-size: 62px; line-height: 1; color: var(--ink); letter-spacing: -1px; }
  .mascot { height: 120px; margin-bottom: 22px; border-radius: 12px; background: linear-gradient(135deg, #a8dc7a, #7cc243); flex: none; }

  .services, .address { font-size: 14px; line-height: 1.4; color: var(--ink); margin-bottom: 16px; white-space: nowrap; }
  .contact { list-style: none; font-size: 14px; color: var(--ink); }
  .contact li { display: flex; align-items: center; gap: 10px; line-height: 1.75; }
  .contact svg { width: 15px; height: 15px; flex: none; }
  .front__rule { height: 2px; background: var(--ink); margin: 12px 0 10px; flex: none; }
  .social { display: flex; gap: 14px; justify-content: flex-end; font-size: 13px; line-height: 1.2; color: var(--green-dark); }
  .social span { display: flex; align-items: center; gap: 5px; }
  .social i { width: 10px; height: 10px; background: var(--green); display: block; }

  /* Back */
  .card--back { left: 630px; background: var(--charcoal); }
  .back__lens { position: absolute; top: 44px; left: 40px; width: 26px; height: 26px; border-radius: 50%; background: #15153a; border: 3px solid #111; }
  .back__mic { position: absolute; top: 53px; left: 80px; width: 8px; height: 8px; border-radius: 50%; border: 1px solid #777; }
  .back__flash { position: absolute; top: 50px; left: 100px; width: 16px; height: 16px; border-radius: 50%; background: #f3e7a6; }
  .back__title { position: absolute; top: 190px; left: 0; right: 0; text-align: center; font-family: "Roboto Condensed", sans-serif; font-weight: 700; font-size: 25px; color: var(--green); }
  .services-grid { position: absolute; top: 260px; left: 30px; right: 30px; display: grid; grid-template-columns: repeat(3, 1fr); row-gap: 40px; column-gap: 18px; }
  .service { text-align: center; }
  .service__photo { height: 96px; border-radius: 12px; margin-bottom: 10px; }
  .service__label { font-family: "Roboto Condensed", sans-serif; font-weight: 700; font-size: 19px; line-height: 1.1; color: var(--white); text-transform: uppercase; }
  .p1 { background: linear-gradient(135deg, #ffffff, #bfc3c7); }
  .p2 { background: linear-gradient(180deg, #f1f6fb, #4fa4d8); }
  .p3 { background: linear-gradient(135deg, #7e8bb8, #3d4570); }
  .p4 { background: linear-gradient(135deg, #ffffff, #8ed06a); }
  .p5 { background: linear-gradient(135deg, #f4d2c0, #3a3a3a); }
  .p6 { background: linear-gradient(135deg, #f2b7b0, #9ea3a8); }
  .makers { position: absolute; bottom: 70px; left: 24px; right: 24px; display: flex; justify-content: center; align-items: center; gap: 10px; font-size: 15px; color: var(--white); }
  .makers .sep { width: 1px; height: 16px; background: var(--white); }
</style>
</head>
<body>

<section class="card card--front" aria-label="Card front">
  <div class="front__sensor"></div>
  <div class="front__camera"></div>
  <div class="front__speaker"></div>
  <div class="front__screen">
    <div class="brand">
      <span class="brand__dot"></span>
      <span class="brand__name">KOBALTO</span>
    </div>
    <div class="mascot" role="img" aria-label="Brand mascot illustration"></div>
    <p class="services">Unlocking &amp; Flashing Services<br>Smart Phones &amp; Accessories Water Damage<br>Screen Repair</p>
    <p class="address">418 Harbor Ave,<br>Fairmont MD 21090</p>
    <ul class="contact">
      <li><svg viewBox="0 0 16 16"><path d="M3 1l3 3-2 2c1 2 3 4 5 5l2-2 3 3-2 3C6 14 2 10 1 3z" fill="var(--green)"/></svg>555.014.2273</li>
      <li><svg viewBox="0 0 16 16"><rect x="1" y="3" width="14" height="10" fill="var(--green)"/><path d="M1 3l7 6 7-6" stroke="#fff" stroke-width="1.5" fill="none"/></svg>info@kobaltorepair.com</li>
      <li><svg viewBox="0 0 16 16"><circle cx="8" cy="8" r="6.5" stroke="var(--green)" stroke-width="1.5" fill="none"/><path d="M1.5 8h13M8 1.5c-3 3-3 10 0 13M8 1.5c3 3 3 10 0 13" stroke="var(--green)" stroke-width="1.2" fill="none"/></svg>www.kobaltostore.com</li>
    </ul>
    <div class="front__rule"></div>
    <div class="social"><span><i></i>gathernest</span><span><i></i>blurvo</span></div>
  </div>
  <div class="front__home"></div>
</section>

<section class="card card--back" aria-label="Card back">
  <div class="back__lens"></div>
  <div class="back__mic"></div>
  <div class="back__flash"></div>
  <h2 class="back__title">CELL PHONE REPAIR SERVICES</h2>
  <div class="services-grid">
    <div class="service"><div class="service__photo p1" role="img" aria-label="Phone with cracked screen"></div><p class="service__label">Cracked<br>Screen</p></div>
    <div class="service"><div class="service__photo p2" role="img" aria-label="Phone splashing in water"></div><p class="service__label">Water<br>Damage</p></div>
    <div class="service"><div class="service__photo p3" role="img" aria-label="Opened phone charging port"></div><p class="service__label">Charging<br>Port</p></div>
    <div class="service"><div class="service__photo p4" role="img" aria-label="Drive with recovery arrow"></div><p class="service__label">Data<br>Recovery</p></div>
    <div class="service"><div class="service__photo p5" role="img" aria-label="Hand holding phone with unlock padlock"></div><p class="service__label">Cell Phone<br>Unlock</p></div>
    <div class="service"><div class="service__photo p6" role="img" aria-label="Tablet being repaired"></div><p class="service__label">Slatra<br>Repair</p></div>
  </div>
  <div class="makers">
    <span>tekvo</span><span class="sep"></span>
    <span>velorin</span><span class="sep"></span>
    <span>plumwick</span><span class="sep"></span>
    <span>dunbelio</span><span class="sep"></span>
    <span>orvan</span>
  </div>
</section>

</body>
</html>
```